Redesign our business card for more impact

We want to completely replace the back design of our card, and refresh or even change the front entirely. We are happy with our black Q7 logo and do not want to change it.
Our company address changed too. It is now 58 Corvallen, Irvine, CA 92741
Updates

It was reported by Sketch Harbor email today that the uploaded files didnt upload. I am trying again.

Target Market(s)

Architects and Building Owners (People making multi-million dollar decisions)

Industry/Entity Type

Consulting Engineering

Contact Information for Business Card

Contact info on the front. "wallpaper" design on back with tag line on the back "Engineering Your Future"

Font styles to use
Sans Serif

Requirements
Must have
• A vivid, modern, impactful ...but tasteful back of card design. It should communicate our premier status, but grab attention as innovative. DESIGN SHOULD BE ELEGANT AND NOT TOO BUSY.
Nice to have
• Repeating pattern, multi-color, something creative...
Should not have
• Anything that looks too playful or that we are not serious professionals. It should also not be too boring or conservative.

```html
<!DOCTYPE html>
<html lang="en">
<head>
<meta charset="utf-8">
<title>Q7 Engineering – Business Card</title>
<link href="https://fonts.googleapis.com/css2?family=Open+Sans:wght@400;700&family=Montserrat:ital,wght@1,700&display=swap" rel="stylesheet">
<style>
  :root {
    --backdrop: #d8d6d7;
    --ink: #333333;
    --paper: #ffffff;
    --muted: #8a8a8a;
    --shadow: rgba(0,0,0,0.35);
  }
  * { margin: 0; padding: 0; box-sizing: border-box; }
  html, body { width: 940px; height: 1200px; overflow: hidden; }
  body { background: var(--backdrop); font-family: "Open Sans", sans-serif; position: relative; }

  .card {
    position: absolute; left: 75px; width: 790px; height: 452px;
    box-shadow: 2px 3px 4px var(--shadow);
  }
  .card-front { top: 124px; background: var(--paper); }
  .card-back { top: 624px; background: var(--ink); overflow: hidden; }

  .wordmark {
    position: absolute; left: 0; width: 100%; text-align: center;
    font-family: "Open Sans", sans-serif; font-weight: 700; line-height: 1;
  }
  .card-front .wordmark { top: 52px; font-size: 150px; color: var(--ink); }
  .card-back .wordmark { top: 112px; font-size: 215px; color: var(--paper); }

  .identity {
    position: absolute; right: 415px; top: 264px; text-align: right; white-space: nowrap;
  }
  .identity .name { font-weight: 700; font-size: 24px; color: var(--ink); letter-spacing: 0.5px; line-height: 30px; }
  .identity .role { font-size: 21px; color: var(--muted); line-height: 28px; }
  .identity .role b { color: var(--ink); font-weight: 700; }

  .divider { position: absolute; left: 394px; top: 261px; width: 1.5px; height: 66px; background: var(--muted); }

  .contacts { position: absolute; left: 413px; top: 252px; list-style: none; }
  .contacts li { display: flex; align-items: center; height: 26px; font-size: 21px; color: var(--muted); white-space: nowrap; }
  .contacts svg { width: 14px; height: 14px; margin-right: 6px; fill: var(--ink); flex: none; }

  .address-band {
    position: absolute; left: 0; top: 384px; width: 100%; height: 37px; background: var(--ink);
  }
  .address-band .address {
    position: absolute; left: 0; width: 788px; top: 0; line-height: 37px; text-align: center;
    color: var(--paper); font-size: 19px;
  }
  .address-band .band-mark {
    position: absolute; left: 640px; top: 0; line-height: 37px;
    color: var(--paper); font-weight: 700; font-size: 26px;
  }

  .back-trim { position: absolute; left: 0; top: 0; width: 790px; height: 452px; }
  .tagline {
    position: absolute; left: 0; width: 100%; top: 409px; text-align: center;
    font-family: "Montserrat", sans-serif; font-style: italic; font-weight: 700;
    font-size: 22px; color: var(--ink); line-height: 30px;
  }
</style>
</head>
<body>

<section class="card card-front">
  <div class="wordmark">Q7</div>

  <div class="identity">
    <p class="name">DANIEL REYES, PE</p>
    <p class="role">HFDP, LEED AP <b>|</b> CEO/Principal</p>
  </div>

  <div class="divider"></div>

  <ul class="contacts">
    <li>
      <svg viewBox="0 0 16 16"><path d="M1 6c0-2 3-3 7-3s7 1 7 3v1h-4V5.5H5V7H1zM3 8h10l1 5H2z"/></svg>
      (626) 555-0142
    </li>
    <li>
      <svg viewBox="0 0 16 16"><path d="M1 6l7-5 7 5v9H1zm2 1v6h10V7L8 10z"/></svg>
      daniel.reyes@q7eng.com
    </li>
    <li>
      <svg viewBox="0 0 16 16"><circle cx="8" cy="8" r="7"/><path d="M5 4c2 0 3 1 2 3s-2 1-3 2M10 10c1-1 3 0 2 2" stroke="#fff" stroke-width="1.4" fill="none"/></svg>
      q7eng.com
    </li>
  </ul>

  <div class="address-band">
    <p class="address">58 Corvallen, Irvine, CA 92741</p>
    <span class="band-mark">Q7</span>
  </div>
</section>

<section class="card card-back">
  <div class="wordmark">Q7</div>

  <svg class="back-trim" viewBox="0 0 790 452" aria-hidden="true">
    <rect x="0" y="440" width="790" height="12" fill="#ffffff"/>
    <polygon points="0,418 157,418 149,427 0,427" fill="#ffffff"/>
    <polygon points="790,418 633,418 641,427 790,427" fill="#ffffff"/>
    <polygon points="186,403 602,403 638,440 150,440" fill="#ffffff"/>
  </svg>

  <p class="tagline">Engineering Your Future</p>
</section>

</body>
</html>
```